Flyer-Design, Thema Kindergeburtstag
Zielgruppe
Wir sind eine Foto-Studio, in dem man auch Kindergeburtstage feiern kann. Infos dazu auf https://plimbofoto.de/kinder-foto-party-kindergeburtstag-witten/
Für die Zielgruppe der Eltern (und deren Kinder) benötigen wir einen Flyer, der unser Angebot umfassend darstellt.
Aufgabenstellung
Unser Angebot 'Kindergeburtstag feiern in Witten' soll bitte visuell für einen Flyer umgesetzt werden.
Da wir recht viel Content (Text und Bild) hierfür bereits besitzen, ist auch ein größerer Flyer (Leporello z.B.) gerne möglich.
Es können alle Bilder und Texte von https://plimbofoto.de/kinder-foto-party-kindergeburtstag-witten/ verwendet werden für den Flyer. Auch unser Logo von PlimboFoto.de
Bauen Sie den Inhalt bitte logisch auf:
1. Was bieten wir (Kindergeburtstage mit vielen verschiedenen Aktionen und Animationen)
2. Wo bieten wir es an (Witten, bei Dortmund)
3. Welche Aktionen und Animationen bieten wir genau an (Auflistung mit einigen passenden Bildern)
4. Buchung und Preise
Folgende Highlights/Themen sollen eine eigene Überschrift oder Spalte bekommen:
- Fotograf und Bilder
- Kostüm-Verleih
- PhotoBooth-System
- Kinder-Schminken
- Hüpfburg
- Sumo-Anzüge und Gladiator-Games
- Image-Video (https://www.vidqueloo.de/watch?v=Tm4rQa8wZpL&feature=emb_title/, siehe https://plimbofoto.de/kinder-foto-party-kindergeburtstag-witten/ oben, Link auch als QR-Code einbinden)
Der Flyer soll schön bunt und phantasievoll werden.
Die Bilder erhalten Sie in hoher Auflösung, wenn nach Vergabe benötigt. Für den ersten Entwurf bitte die Bilder auf https://plimbofoto.de/kinder-foto-party-kindergeburtstag-witten/ einfach downloaden.
Logo-Download:
https://ablage.wolkenfach.de/open?id=7Hq2mRt9Lx4bWcP8Vn3Ks6Yd1Zf5Gj0Ae
https://ablage.wolkenfach.de/open?id=3k_TpQWEN84sLfRZ2m7GaYcBx_u-PD

```html
<!DOCTYPE html>
<html lang="de">
<head>
<meta charset="utf-8">
<title>Kindergeburtstag Faltflyer – Innenseite</title>
<link href="https://fonts.googleapis.com/css2?family=Montserrat:wght@300;400;600;700;800&display=swap" rel="stylesheet">
<style>
  :root{
    --stage:#5f5c66;
    --paper:#ffffff;
    --ink:#1c1a22;
    --pink:#e8336d;
    --pink-soft:#f26a93;
    --purple:#8a3fa8;
    --lilac:#b98acb;
    --sky:#6fb7ef;
    --frame:#2b2730;
  }
  *{box-sizing:border-box;margin:0;padding:0}
  html,body{width:1200px;height:857px;overflow:hidden}
  body{background:var(--stage);font-family:"Montserrat",sans-serif;color:var(--ink);position:relative}
  .leporello{position:absolute;left:36px;top:158px;width:1128px;height:540px;display:flex;box-shadow:0 20px 40px rgba(0,0,0,.35)}
  .panel{position:relative;width:376px;height:540px;background:var(--paper);overflow:hidden}
  .panel + .panel{border-left:1px solid #ececec}
  .photo{position:absolute;overflow:hidden}
  .blob{position:absolute}

  /* Panel 1 */
  .p1-band{position:absolute;left:0;top:0;width:376px;height:540px}
  .p1-girl{left:0;top:95px;width:300px;height:445px;border-radius:0 60px 0 0;
    background:linear-gradient(160deg,#2d3f9e 0%,#5a7fd6 40%,#e7b98c 70%,#d8d0d6 100%)}
  .p1-boy{left:205px;top:20px;width:150px;height:190px;border-radius:70px 70px 30px 80px;
    background:linear-gradient(180deg,#f4c53a 0%,#e9c3a3 45%,#2d4f9c 100%)}
  .p1-balloons{left:262px;top:300px;width:114px;height:240px;border-radius:60px 0 0 0;
    background:radial-gradient(circle at 40% 30%,#c98ae0 0%,#8a3fa8 45%,#6fb7ef 100%)}
  .badge{position:absolute;left:205px;top:125px;width:110px;height:110px;border-radius:50%;background:var(--paper);display:flex;align-items:center;justify-content:center}
  .badge span{width:80px;height:80px;border-radius:50%;background:var(--lilac)}

  /* Panel 2 */
  .intro{position:absolute;left:28px;top:36px;right:22px}
  .intro h1{font-size:15px;line-height:1.15;font-weight:300;letter-spacing:-.3px}
  .intro h1 b{font-weight:800}
  .intro h1 em{font-style:normal;font-weight:800;color:var(--pink)}
  .intro .kicker{margin-top:4px;font-size:11px;font-weight:800;color:var(--pink);text-transform:uppercase;letter-spacing:-.2px}
  .intro .lead{margin-top:4px;font-size:5.5px;line-height:1.3}
  .offers{list-style:none;margin-top:8px}
  .offers li{font-size:6.5px;font-weight:700;text-transform:uppercase;line-height:1.3;margin-bottom:6px}
  .offers li.hl{color:var(--pink)}
  .new-title{position:absolute;left:60px;top:196px;font-size:20px;font-weight:300;letter-spacing:-.5px}
  .new-title em{font-style:normal;font-weight:800;color:var(--pink)}
  .grid{position:absolute;left:62px;top:232px;width:296px;height:258px}
  .tile{position:absolute;border:4px solid var(--frame)}
  .tile.pink{border-color:var(--pink)}
  .cap{position:absolute;background:#fff;font-size:5.5px;font-weight:700;text-transform:uppercase;line-height:1.25;padding:3px 5px;color:var(--ink)}
  .t-boulder{left:0;top:0;width:108px;height:258px;background:linear-gradient(180deg,#efe6e2 0%,#d9c2b8 60%,#e23b3b 82%,#3b8de0 100%)}
  .t-bounce{left:112px;top:0;width:106px;height:122px;background:linear-gradient(160deg,#e8336d,#f5a623 50%,#3aa0e8)}
  .t-sumo{left:222px;top:0;width:74px;height:122px;background:linear-gradient(180deg,#1f3f7a,#d9a441)}
  .t-safari{left:112px;top:126px;width:106px;height:132px;background:linear-gradient(180deg,#7a8a4a,#b39a6e 60%,#4e5a34)}
  .t-hero{left:222px;top:126px;width:74px;height:132px;background:linear-gradient(180deg,#3a62b5,#c8403e)}

  /* Panel 3 */
  .p3-woman{left:190px;top:50px;width:186px;height:440px;border-radius:90px 0 0 110px;
    background:linear-gradient(180deg,#b8d0e6 0%,#e7c2a8 30%,#d0314a 60%,#8fa9c2 100%)}
  .p3-cakes{left:250px;top:0;width:126px;height:50px;background:linear-gradient(180deg,#e8336d,#7a3b2a)}
  .p3-kid{left:40px;top:395px;width:120px;height:145px;border-radius:60px 60px 0 0;
    background:linear-gradient(180deg,#15151a 0%,#3a3a44 60%,#cc2233 100%)}
  .info{position:absolute;left:18px;top:38px;width:180px}
  .info h2{font-size:13px;font-weight:300;line-height:1.1}
  .info h2 em{font-style:normal;font-weight:800;color:var(--pink)}
  .info p{font-size:5.6px;line-height:1.45;margin-top:5px}
  .info .rent{margin-top:18px}
  .price-label{font-size:7px;font-weight:800;margin-top:5px}
  .price{font-size:13px;font-weight:800;color:var(--pink);line-height:1.1}
  .link{font-size:5.6px;color:var(--pink);font-weight:600}
</style>
</head>
<body>
<main class="leporello">

  <section class="panel panel-cover">
    <svg class="p1-band" viewBox="0 0 376 540" aria-hidden="true">
      <path d="M0 150 C60 110 140 90 200 60 C230 45 250 30 270 0 L376 0 L376 40 C330 60 300 110 320 180 C340 250 300 310 280 300 L0 300 Z" fill="#e8336d"/>
      <path d="M150 0 C170 30 200 40 240 20 L250 0 Z" fill="#f26a93"/>
    </svg>
    <div class="photo p1-girl" role="img" aria-label="Mädchen mit Schmetterlings-Kinderschminken und Fühlern, sitzt auf einem Reifen vor bunter Lichtwand"></div>
    <div class="photo p1-boy" role="img" aria-label="Kleiner Junge im Feuerwehrkostüm mit gelbem Helm und Wasserspritze"></div>
    <div class="photo p1-balloons" role="img" aria-label="Glänzende Luftballons in Lila, Blau und Gold"></div>
    <div class="badge" aria-label="Auszeichnung"><span></span></div>
  </section>

  <section class="panel panel-offer">
    <div class="intro">
      <h1><b>Kindergeburtstag,</b> Best-Friend-Party, JGA, Disco-Dance-Party, <em>sonstige Events im Foto-Studio Witten feiern.</em></h1>
      <p class="kicker">Mehr als 20 Aktionen für deine Party.</p>
      <p class="lead">Die Location (bis ca. 20 Personen) mit den buntesten Aktionen, Animationen und Foto-Motto-Partys im ganzen Ruhrgebiet</p>
      <ul class="offers">
        <li>Kostüme (neuwertige Wunsch-Kostüme in benötigter Größe)</li>
        <li class="hl">PhotoBooth/ Foto-Box (Selbstauslöser-Kamera inkl. Drucker)</li>
        <li>Bilder digital. Die von uns im Studio fotografierten Bilder werden also nicht extra berechnet.</li>
        <li class="hl">Ohne Aufpreis: Lumbra-Fotobuch (Hardcover, Premium-Papier, 30 Seiten, inkl. Gestaltung) bei Buchung des Fotografen für mindestens drei Stunden</li>
      </ul>
    </div>
    <h2 class="new-title">Jetzt neu <em>für deine Party</em></h2>
    <div class="grid">
      <div class="tile t-boulder" role="img" aria-label="Boulder-Kletterwand mit Bällebad">
        <span class="cap" style="left:6px;top:8px;right:6px">Boulder-Kletterwand (2 Meter breit, 3 Meter hoch) mit weicher Sprungmatte</span>
      </div>
      <div class="tile pink t-bounce" role="img" aria-label="Kinder in einer bunten Hüpfburg">
        <span class="cap" style="left:6px;bottom:8px;right:6px">Hüpfburg, 400 x 300 cm und Hüpfburg mit Rutsche, 300 x 300 cm</span>
      </div>
      <div class="tile t-sumo" role="img" aria-label="Kinder in Sumo-Anzügen"></div>
      <div class="tile t-safari" role="img" aria-label="Kinder mit Safarihüten beim Fotografieren">
        <span class="cap" style="left:6px;bottom:10px;right:6px">Foto-Workshop + Fotosafari für Kinder (Infos siehe unten)</span>
      </div>
      <div class="tile pink t-hero" role="img" aria-label="Kinder in Superhelden-Kostümen">
        <span class="cap" style="left:5px;bottom:10px;right:5px">Sumo-Anzüge und Gladiator Games</span>
      </div>
    </div>
  </section>

  <section class="panel panel-booth">
    <svg class="blob" style="left:0;top:0" width="376" height="540" viewBox="0 0 376 540" aria-hidden="true">
      <path d="M170 0 L376 0 L376 60 C300 40 250 70 240 120 C230 170 200 200 180 190 C200 120 180 60 170 0 Z" fill="#e8336d"/>
    </svg>
    <div class="photo p3-cakes" role="img" aria-label="Schokoladen-Cupcakes mit Sahnehaube"></div>
    <div class="photo p3-woman" role="img" aria-label="Frau mit Partybrille und bunter Federboa vor gepunkteten Luftballons und Fotobox"></div>
    <div class="info">
      <h2>Leihkamera und <em>PhotoBooth -System (Foto-Box)</em></h2>
      <p>Gerne stellen wir Ihnen eine Leihkamera oder ein PhotoBooth-System (Kamera + Blitz + Selbstauslöser) zur Verfügung. Wir verleihen zwei verschiedene PhotoBooth-Systeme: Kompakt-Box ohne Drucker (Speicherung auf Karte und in Cloud) sowie die wesentlich größere Print-Box inkl. dem Top-Endlos-Drucker KX-40 (Print in 10x15 + Speicherung auf Karte und in Cloud). Die Boxen stehen Ihnen bei unseren Veranstaltungen im Studio ohne Aufpreis zur Verfügung.</p>
      <div class="rent">
        <h2>Vermietung <em>PhotoBooth Witten</em></h2>
        <p>Die Foto-Boxen können auch gerne unabhängig von einer Veranstaltung bei uns gemietet werden.</p>
        <p class="price-label">Mietpreis je Tag</p>
        <p class="price">ab 119 Euro inkl. Ust.</p>
        <p>Weitere Informationen zur Vermietung unserer PhotoBooth-Systeme auf</p>
        <p class="link">plimbofoto.de/photobooth-photobox-witten</p>
      </div>
    </div>
    <div class="photo p3-kid" role="img" aria-label="Kind in dunklem Weltraum-Kostüm mit rotem Lichtschwert"></div>
  </section>

</main>
</body>
</html>
```